female esthetician looking for an impact business card

I an an expert in skin care industry with high experience in NYC.I want my business card to look professional , an impact at first look. I do want a combination between white and gold . I believe the font will be great if is gold.. The Fonts are also important. MARISELA VONDRAKE (SKIN CARE BOUTIQUE)

THIS SHOULD BE THE BUSINESS NAME, and should be placed on th eback of the card.
IN front m, the name MARISELA VONDRAKE - ESTHETCIAN

BY APPOINTMENTS ONLY: 555.218.9031

Target Market(s)

HIGH END CLIENTELE

Contact Information for Business Card

iT WILL BE on a luxury paper. I neeed the wow feeling

Requirements
Should not have
• pictures

```html
<!DOCTYPE html>
<html lang="en">
<head>
<meta charset="utf-8">
<title>Marisela Vondrake – Business Card</title>
<link rel="stylesheet" href="https://fonts.googleapis.com/css2?family=Cinzel:wght@500;600&family=Josefin+Sans:wght@300;400&family=Montserrat:wght@300;400&display=swap">
<style>
  :root {
    --stage: #e4e4e4;
    --card-blue: #d9e1ea;
    --panel-white: #f4f5f7;
    --gold-light: #f1d27a;
    --gold: #c9993a;
    --gold-deep: #a97a24;
    --ink-grey: #6f6f74;
    --icon-rose: #c98a94;
    --petal-pink: #e7a9b6;
    --petal-cream: #f6dccd;
    --leaf-slate: #9aa9bd;
  }
  * { box-sizing: border-box; margin: 0; padding: 0; }
  html, body {
    width: 1200px; height: 1000px; overflow: hidden;
    background: var(--stage);
  }
  .canvas {
    position: relative; width: 1200px; height: 1000px;
    display: flex; align-items: center; justify-content: center;
  }
  .business-card {
    position: relative; width: 900px; height: 514px;
    background: var(--card-blue);
    overflow: hidden;
    box-shadow: 0 18px 40px rgba(0,0,0,0.12);
  }
  .floral {
    position: absolute;
    border-radius: 50%;
    filter: blur(2px);
  }
  .floral--left {
    left: -60px; top: 160px; width: 200px; height: 280px;
    background:
      radial-gradient(circle at 45% 40%, var(--petal-pink) 0 30%, transparent 55%),
      radial-gradient(circle at 60% 72%, var(--petal-cream) 0 26%, transparent 50%),
      radial-gradient(circle at 30% 20%, var(--leaf-slate) 0 14%, transparent 40%);
  }
  .floral--right {
    right: -70px; top: -20px; width: 330px; height: 500px;
    background:
      radial-gradient(circle at 48% 28%, var(--petal-pink) 0 26%, transparent 46%),
      radial-gradient(circle at 22% 14%, var(--petal-cream) 0 14%, transparent 30%),
      radial-gradient(circle at 62% 58%, var(--petal-cream) 0 18%, transparent 36%),
      radial-gradient(circle at 58% 82%, rgba(231,169,182,0.7) 0 12%, transparent 28%),
      radial-gradient(circle at 30% 60%, var(--leaf-slate) 0 12%, transparent 34%);
    z-index: 2;
  }
  .info-panel {
    position: absolute; left: 150px; top: 60px; width: 570px; height: 400px;
    background: var(--panel-white);
    z-index: 1;
  }
  .gold-frame {
    position: absolute; inset: 22px;
    border: 5px solid var(--gold);
    border-image: linear-gradient(135deg, var(--gold-deep), var(--gold-light) 45%, var(--gold) 70%, var(--gold-light)) 1;
    z-index: 3;
  }
  .identity {
    position: absolute; left: 205px; top: 118px; width: 470px; z-index: 4;
  }
  .identity__name, .identity__title {
    background: linear-gradient(180deg, var(--gold-light), var(--gold) 55%, var(--gold-deep));
    -webkit-background-clip: text; background-clip: text;
    color: transparent;
  }
  .identity__name {
    font-family: "Cinzel", serif; font-weight: 600;
    font-size: 37px; letter-spacing: 0; line-height: 1.1;
    white-space: nowrap;
  }
  .identity__title {
    font-family: "Josefin Sans", sans-serif; font-weight: 400;
    font-size: 29px; letter-spacing: 1.5px; margin-top: 4px;
    padding-left: 40px;
  }
  .contact-list {
    position: absolute; left: 250px; top: 270px; z-index: 4;
    list-style: none;
    font-family: "Montserrat", sans-serif; font-weight: 300;
    font-size: 18px; color: var(--ink-grey); line-height: 1.35;
  }
  .contact-list li { display: flex; align-items: flex-start; gap: 10px; margin-bottom: 6px; }
  .contact-list svg { width: 16px; height: 16px; flex: none; margin-top: 3px; }
</style>
</head>
<body>
<main class="canvas">
  <article class="business-card">
    <div class="floral floral--left" role="img" aria-label="Pink and cream floral illustration with slate leaves"></div>
    <section class="info-panel">
      <div class="gold-frame"></div>
    </section>
    <div class="floral floral--right" role="img" aria-label="Large pink blossom bouquet with cream flowers and slate leaves"></div>

    <header class="identity">
      <h1 class="identity__name">MARISELA VONDRAKE</h1>
      <p class="identity__title">skin care expert</p>
    </header>

    <ul class="contact-list">
      <li>
        <svg viewBox="0 0 16 16" aria-hidden="true"><path fill="var(--icon-rose)" d="M3.2 1.5l2.3 2.6-1.2 1.6c.9 2 2.4 3.5 4.2 4.3l1.6-1.2 2.6 2.3-1.3 2.1C6.6 13 2.9 9.3 1.1 4.6z"/></svg>
        <span>+1.555.218.9031</span>
      </li>
      <li>
        <svg viewBox="0 0 16 16" aria-hidden="true"><rect x="1.5" y="3.5" width="13" height="9" fill="none" stroke="var(--icon-rose)" stroke-width="1.4"/><path d="M1.5 3.5L8 9l6.5-5.5" fill="none" stroke="var(--icon-rose)" stroke-width="1.4"/></svg>
        <span>info@mariselavondrake.com</span>
      </li>
      <li>
        <svg viewBox="0 0 16 16" aria-hidden="true"><path fill="var(--icon-rose)" d="M8 1a5 5 0 0 0-5 5c0 3.6 5 9 5 9s5-5.4 5-9a5 5 0 0 0-5-5zm0 7a2 2 0 1 1 0-4 2 2 0 0 1 0 4z"/></svg>
        <span>Level 4, 12 Alder Street<br>Brookfield, Australia</span>
      </li>
    </ul>
  </article>
</main>
</body>
</html>
```